Web Design Front Page Only for Organic Skincare

We have been in business for nearly 20 years. We are run by all females and sell anything from aromatherapy, skincare and pharmacy types products to health food shops and pharmacy. We are looking for an attractive and colourful but simple front web page design for our wholesale customers to look at. We want our customers to start using our website to find information rather than ringing us. So we want it to be attractive to our buyers who are young and funky.
Updates

To give you an idea of the products we sell to pharmacy and health food shops also beauty shops and hair salons.  We mainly deal with organic body and skincare, aromatherapy oils and body products, but also do some simple pharmacy products such as bandages and pill boxes, finger splits, walking frames and wheelchairs.  We are only looking for the front page of the website.  The back-end will be done in-house.  We currently do not have a logo designed so I am thinking that once we have done the website design we can build a logo from it.  I like bright colours and want something that is inviting to further discover that we do many different types of products.

Target Market(s)

young girls who are our retail buyers

Industry/Entity Type

Pharmacy

Requirements
Must have
• A section which says

Customer Log in
Should not have
• don't worry about too much writing or tabs. We will insert these later. Just come up with design image.

```html
<!DOCTYPE html>
<html lang="en">
<head>
<meta charset="utf-8">
<title>Verdelle Healthcare</title>
<link rel="stylesheet" href="https://fonts.googleapis.com/css2?family=Libre+Baskerville:wght@700&family=Noto+Sans:wght@400;600;700&display=swap">
<style>
:root{
  --green:#6e9a0a;
  --green-dark:#4f7405;
  --green-light:#8cb424;
  --title:#e8f3a6;
  --white:#ffffff;
  --ink:#1e1e1e;
  --pale:#fdf9e4;
  --footer:#6c9a05;
}
*{box-sizing:border-box;margin:0;padding:0}
html,body{width:883px;height:1200px;overflow:hidden}
body{position:relative;font-family:"Noto Sans",sans-serif;background:var(--white);color:var(--ink)}
.header{position:absolute;left:0;top:0;width:883px;height:126px;
  background:linear-gradient(90deg,var(--green-dark) 0%,var(--green) 20%,var(--green-light) 50%,var(--green) 80%,var(--green-dark) 100%)}
.cart{position:absolute;left:675px;top:0;width:164px;height:33px;background:#3e5410;border-radius:0 0 4px 4px;
  color:var(--title);font-size:16px;display:flex;align-items:center;gap:8px;padding-left:12px}
.brand-title{position:absolute;left:0;width:917px;top:52px;text-align:center;font-family:"Libre Baskerville",serif;
  font-size:31px;color:var(--title);letter-spacing:1px}
.logo{position:absolute;left:34px;top:74px;font-size:35px;color:var(--white)}
.search{position:absolute;left:680px;top:93px;width:159px;height:26px;border-radius:13px;background:#3b4f0d;
  color:var(--white);font-size:13px;display:flex;align-items:center;justify-content:space-between;padding:0 10px 0 12px}
.nav{position:absolute;left:0;top:126px;width:883px;height:43px;background:var(--white);display:flex;align-items:center;padding-left:29px}
.nav a{font-size:13px;color:var(--green-dark);text-decoration:none;padding:0 5px;line-height:43px;font-weight:600}
.nav a.active{background:var(--green);color:var(--white);padding:0 5px}
.hero{position:absolute;left:0;top:169px;width:883px;height:926px;
  background:linear-gradient(170deg,#c7cfa6 0%,#eef2f6 18%,#a9c4ec 35%,#e6eef8 50%,#6f86b0 62%,#8c9392 78%,#6e7470 100%)}
.frame-line{position:absolute;top:169px;width:8px;height:926px;background:var(--white)}
.sidebar{position:absolute;left:34px;top:169px;width:238px;height:926px;background:rgba(255,255,255,.72)}
.hero-text{position:absolute;left:527px;top:172px;font-size:48px;color:var(--white)}
.section-title{position:absolute;left:39px;font-size:21px;color:var(--green);width:222px;border-bottom:1px solid var(--ink);line-height:1.2}
.product{position:absolute;left:39px;width:231px;height:50px}
.product.active{background:var(--green)}
.thumb{position:absolute;left:0;top:0;width:76px;height:50px;border:2px solid #ddd}
.product .name{position:absolute;left:82px;top:-2px;font-size:24px;color:var(--green)}
.product .sub{position:absolute;top:24px;font-size:16px;color:var(--green)}
.product.active .name,.product.active .sub{color:var(--white)}
.chev{position:absolute}
.dropdown{position:absolute;left:274px;top:233px;width:112px}
.dropdown div{height:19px;border:1px solid #eadfa6;background:var(--pale);font-size:12px;text-align:center;color:#4a4a3a;line-height:17px}
.label{position:absolute;left:42px;font-size:13px;font-weight:700}
.input{position:absolute;left:43px;width:219px;height:27px;border-radius:6px;border:1px solid #ccc;background:var(--white)}
.forgot{position:absolute;left:48px;top:830px;font-size:11px}
.btn{position:absolute;background:var(--green);color:var(--white);border-radius:4px;text-align:center}
.footer{position:absolute;left:0;top:1095px;width:883px;height:105px;background:var(--footer);color:var(--white)}
.connect{position:absolute;left:39px;top:12px;font-size:13px;font-weight:600}
.social{position:absolute;top:12px;width:20px;height:20px;border-radius:2px}
.foot-links{position:absolute;right:44px;top:11px;display:flex;font-size:11px}
.foot-links span{padding:0 3px;border-left:1px solid var(--white)}
.foot-links span:first-child{border-left:none}
.copyright{position:absolute;right:47px;top:64px;font-size:11px}
</style>
</head>
<body>
<header class="header">
  <div class="cart">
    <svg width="20" height="18" viewBox="0 0 20 18"><path d="M1 2h3l2 9h10l2-7H5" fill="none" stroke="#e8f3a6" stroke-width="2"/><circle cx="8" cy="15" r="1.7" fill="#e8f3a6"/><circle cx="15" cy="15" r="1.7" fill="#e8f3a6"/></svg>
    Cart 0 items
  </div>
  <div class="brand-title">VERDELLE HEALTHCARE</div>
  <div class="logo">Logo</div>
  <div class="search">Searching.....
    <svg width="18" height="18" viewBox="0 0 18 18"><circle cx="7" cy="7" r="5" fill="none" stroke="#fff" stroke-width="2.2"/><path d="M11 11l5 5" stroke="#fff" stroke-width="3"/></svg>
  </div>
</header>
<nav class="nav">
  <a class="active">Home</a><a>About Us</a><a>Products</a><a>Health Foods</a><a>Pharmacy</a><a>Supermarket</a><a>Beauty</a><a>Contact Us</a>
</nav>

<div class="hero" role="img" aria-label="Photograph of a waterfall cascading over rocks"></div>
<div class="frame-line" style="left:26px"></div>
<div class="frame-line" style="left:845px"></div>
<div class="sidebar"></div>
<div class="hero-text">Text</div>

<div class="section-title" style="top:178px">Our Products</div>

<div class="product active" style="top:216px">
  <div class="thumb" role="img" aria-label="Cosmetic bottles" style="background:linear-gradient(#f3efe2,#d9c99a)"></div>
  <div class="name">Cosmetics</div><div class="sub" style="left:146px">Products</div>
  <svg class="chev" style="left:208px;top:8px" width="14" height="10" viewBox="0 0 14 10"><path d="M2 2l5 5 5-5" fill="none" stroke="#fff" stroke-width="2.5"/></svg>
</div>
<div class="dropdown"><div>Skin Cream</div><div>Body Oil</div><div>Lip balm</div><div>Moisturiser</div></div>

<div class="product" style="top:280px">
  <div class="thumb" role="img" aria-label="Pill box" style="background:linear-gradient(#f4f6fa,#3d6bb5)"></div>
  <div class="name">Pharmacy</div><div class="sub" style="left:146px">Products</div>
  <svg class="chev" style="left:202px;top:6px" width="10" height="14" viewBox="0 0 10 14"><path d="M2 2l5 5-5 5" fill="none" stroke="#fff" stroke-width="2.5"/></svg>
</div>
<div class="product" style="top:343px">
  <div class="thumb" role="img" aria-label="Aloe vera plant" style="background:linear-gradient(#e8efe0,#4f8a2e)"></div>
  <div class="name">Herbal</div><div class="sub" style="left:146px">Medicines</div>
</div>
<div class="product" style="top:407px">
  <div class="thumb" role="img" aria-label="Wheelchair" style="background:linear-gradient(#f5f5f5,#9a9a9a)"></div>
  <div class="name">Wheelchair</div>
</div>
<div class="product" style="top:476px">
  <div class="thumb" role="img" aria-label="Walking frame" style="background:linear-gradient(#fafafa,#b8b8b8)"></div>
  <div class="name">Walking</div><div class="sub" style="left:146px">frames</div>
</div>
<div class="product" style="top:545px">
  <div class="thumb" role="img" aria-label="Finger splint on a hand" style="background:linear-gradient(#2e5f86,#d9a98a)"></div>
  <div class="name">Finger</div><div class="sub" style="left:146px">splits</div>
</div>
<div class="product" style="top:607px">
  <div class="thumb" role="img" aria-label="Lavender flowers" style="background:linear-gradient(#f2f0f6,#6f5fa6)"></div>
  <div class="name">Health</div><div class="sub" style="left:146px">Food</div>
</div>

<div class="section-title" style="top:677px">Customers Login</div>
<div class="label" style="top:716px">Username</div>
<div class="input" style="top:734px"></div>
<div class="label" style="top:765px">Password</div>
<div class="input" style="top:783px"></div>
<div class="forgot">Forgot Password ?</div>
<div class="btn" style="left:158px;top:825px;width:93px;height:24px;font-size:16px;line-height:24px">Log in</div>
<div class="btn" style="left:44px;top:867px;width:216px;height:20px;font-size:13px;line-height:20px;font-weight:600">Sign Up For New Member</div>

<footer class="footer">
  <div class="connect">Connect With Us:</div>
  <div class="social" style="left:160px;background:#3b5b9a"></div>
  <div class="social" style="left:186px;background:#3fb4e0"></div>
  <div class="social" style="left:212px;background:#1d7ab5"></div>
  <div class="social" style="left:238px;background:#f08a1c"></div>
  <div class="foot-links"><span>Home</span><span>About Us</span><span>Products</span><span>Health Foods</span><span>Pharmacy</span><span>Supermarket</span><span>Beauty</span><span>Contact Us</span></div>
  <div class="copyright">Copyright © 2012 By Company.All Right Reserved</div>
</footer>
</body>
</html>
```